Tor'k Wayfarer Travel

We need a sleek, professional, inviting card to elicit global travel for the experienced and professional traveler. Royal blue, black and silver. (perhaps the wording could be silver with black shadow?-get creative) Maybe a watermark on the front and the full raised logo on the back.
We want a stylish and modern card, but professional.

```html
<!DOCTYPE html>
<html lang="en">
<head>
<meta charset="utf-8">
<title>Tor'k Wayfarer Travel – Business Card</title>
<link href="https://fonts.googleapis.com/css2?family=Montserrat:wght@600;700;800&display=swap" rel="stylesheet">
<style>
  :root {
    --page-bg: #ffffff;
    --card-bg: #000000;
    --silver: #c9c9c9;
    --white: #ffffff;
    --caption: #111111;
  }
  html, body {
    margin: 0;
    padding: 0;
    width: 1200px;
    height: 1000px;
    overflow: hidden;
    background: var(--page-bg);
  }
  .canvas {
    position: relative;
    width: 1200px;
    height: 1000px;
  }
  .card {
    position: absolute;
    left: 244px;
    width: 712px;
    height: 407px;
    background: var(--card-bg);
    font-family: 'Montserrat', sans-serif;
  }
  .card--front { top: 70px; }
  .card--back { top: 524px; }

  .brand-name {
    position: absolute;
    left: 0;
    right: 0;
    top: 190px;
    margin: 0;
    text-align: center;
    color: var(--silver);
    font-weight: 600;
    font-size: 36px;
    line-height: 40px;
    letter-spacing: 0.5px;
    text-transform: uppercase;
  }
  .brand-name .line { display: block; }
  .brand-name .line--sub { font-size: 28px; letter-spacing: 6px; }
  .brand-dot {
    position: absolute;
    left: 346px;
    top: 150px;
    width: 20px;
    height: 20px;
    border-radius: 50%;
    background: var(--silver);
  }
  .website {
    position: absolute;
    left: 0;
    right: 0;
    top: 334px;
    text-align: center;
    color: var(--white);
    font-weight: 700;
    font-size: 19px;
    letter-spacing: 1px;
  }

  .contact { position: absolute; left: 51px; color: var(--white); }
  .person-name {
    top: 168px;
    margin: 0;
    font-weight: 800;
    font-size: 34px;
    letter-spacing: 1.5px;
  }
  .person-role {
    top: 217px;
    margin: 0;
    font-weight: 700;
    font-size: 19.5px;
    letter-spacing: 0.8px;
  }
  .details {
    top: 278px;
    margin: 0;
    padding: 0;
    list-style: none;
    font-weight: 700;
    font-size: 16.5px;
    letter-spacing: 0.7px;
    line-height: 29px;
  }

  .caption {
    position: absolute;
    left: 0;
    right: 0;
    top: 956px;
    margin: 0;
    text-align: center;
    color: var(--caption);
    font-family: Arial, Helvetica, sans-serif;
    font-size: 20px;
  }
</style>
</head>
<body>
<div class="canvas">
  <section class="card card--front" aria-label="Card front">
    <span class="brand-dot" aria-hidden="true"></span>
    <h1 class="brand-name">
      <span class="line">Tor'k Wayfarer</span>
      <span class="line line--sub">Travel</span>
    </h1>
    <div class="website">www.samplewebsite.com</div>
  </section>

  <section class="card card--back" aria-label="Card back">
    <h2 class="contact person-name">SAMPLE NAME</h2>
    <p class="contact person-role">Sample Position</p>
    <ul class="contact details">
      <li>123-456-7890</li>
      <li>sampleemail@gmail.com</li>
      <li>Sample Address, Unit #, City, 12345</li>
    </ul>
  </section>

  <p class="caption">Black Business Card + Silver Foil on Logo + White Foil on Text</p>
</div>
</body>
</html>
```